All Natural Raw Honey & Goats Milk Body Wash Labels

We have launched a new product line of all natural Raw Honey & Goats Milk body wash with the business name being Dawn Meadow and the tag line Naturally . Their are currently three line items requiring three labels. Natural (Unscented), Japanese Honeysuckle and Caribbean.
It is a family orientated product that we want to promote as being all natural, healthy and trustworthy. It is an all Australian made product that uses our very own award winning raw honey
I can supply the file for the business name/logo upon request

Target Market(s)

Families

Industry/Entity Type

Bath & body

Requirements
Must have
• a Lux high end feel
Nice to have
• simple easy to read with minimal images
Should not have
• No cartoons

```html
<!DOCTYPE html>
<html lang="en">
<head>
<meta charset="utf-8">
<title>Dawn Meadow Body Wash Labels</title>
<link href="https://fonts.googleapis.com/css2?family=Barlow+Condensed:wght@400;500&family=Bodoni+Moda:opsz,wght@6..96,500&display=swap" rel="stylesheet">
<style>
  :root {
    --page: #f7f7f7;
    --gold-light: #eeeec4;
    --gold-mid: #dcdb9e;
    --gold-band: #bfa91a;
    --gold-band-hi: #dccd2a;
    --gold-ink: #7a6a12;
    --gold-accent: #f0e040;
    --teal-light: #d3efee;
    --teal-mid: #b5e0df;
    --teal-band: #1f5f5d;
    --teal-band-hi: #3aa8a5;
    --teal-ink: #1d4a48;
    --teal-accent: #3fe0e0;
    --green-light: #daf0d6;
    --green-mid: #bfe3b9;
    --green-band: #1d8a35;
    --green-band-hi: #3bc657;
    --green-ink: #1a5c2a;
    --green-accent: #4cf06a;
    --white: #ffffff;
  }
  * { box-sizing: border-box; margin: 0; padding: 0; }
  html, body { width: 1200px; height: 842px; overflow: hidden; background: var(--page); }
  .canvas {
    width: 1200px; height: 842px; display: flex; justify-content: center;
    align-items: center; gap: 90px;
  }
  .label {
    position: relative; width: 270px; height: 640px; overflow: hidden;
    font-family: "Barlow Condensed", sans-serif;
    background: var(--light);
  }
  .label--honeysuckle { --light: var(--gold-light); --mid: var(--gold-mid); --band: var(--gold-band); --band-hi: var(--gold-band-hi); --ink: var(--gold-ink); --accent: var(--gold-accent); }
  .label--caribbean { --light: var(--teal-light); --mid: var(--teal-mid); --band: var(--teal-band); --band-hi: var(--teal-band-hi); --ink: var(--teal-ink); --accent: var(--teal-accent); }
  .label--natural { --light: var(--green-light); --mid: var(--green-mid); --band: var(--green-band); --band-hi: var(--green-band-hi); --ink: var(--green-ink); --accent: var(--green-accent); }

  .label__pattern {
    position: absolute; inset: 0;
    background: linear-gradient(160deg, var(--light) 0%, var(--mid) 45%, var(--light) 100%);
  }
  .brand {
    position: absolute; top: 190px; left: 0; right: 0; text-align: center;
    font-size: 30px; font-weight: 500; color: var(--ink); letter-spacing: 1px;
  }
  .band {
    position: absolute; top: 330px; left: 8px; right: 8px; height: 215px;
    background: linear-gradient(100deg, var(--band) 0%, var(--band-hi) 55%, var(--band) 100%);
    border-top: 5px solid var(--accent);
    padding: 22px 0 0 22px; color: var(--white);
  }
  .band__variant {
    font-size: 17px; font-weight: 500; color: var(--accent); letter-spacing: 1px;
  }
  .band__variant--spaced { letter-spacing: 9px; }
  .band__title {
    font-family: "Bodoni Moda", serif; font-weight: 500;
    font-size: 62px; line-height: 0.95; margin-top: 8px; letter-spacing: -2px;
    transform: scaleX(0.82); transform-origin: left;
  }
  .band__art {
    position: absolute; right: 12px; top: 24px; width: 60px; height: 175px;
    background: linear-gradient(180deg, rgba(255,255,255,.45), rgba(255,255,255,.15));
    border-radius: 30px;
  }
  .details { position: absolute; top: 560px; left: 0; right: 0; text-align: center; color: var(--ink); }
  .details__claim { font-size: 17px; font-weight: 500; letter-spacing: .3px; }
  .details__map {
    display: block; width: 14px; height: 12px; margin: 14px auto 8px;
    background: var(--ink); border-radius: 40% 50% 45% 35%;
  }
  .details__origin { font-size: 13px; font-weight: 500; }
  .details__volume { font-size: 13px; margin-top: 10px; }
</style>
</head>
<body>
<main class="canvas">

  <article class="label label--honeysuckle">
    <div class="label__pattern" role="img" aria-label="Faint white honeysuckle flower and leaf pattern"></div>
    <div class="brand">Dawn Meadow</div>
    <section class="band">
      <p class="band__variant">JAPANESE HONEYSUCKLE</p>
      <h2 class="band__title">BODY<br>WASH</h2>
      <div class="band__art" role="img" aria-label="White line drawing of a honeysuckle sprig"></div>
    </section>
    <footer class="details">
      <p class="details__claim">NATURAL RAW HONEY &amp; GOATS MILK</p>
      <span class="details__map" role="img" aria-label="Small map of Australia"></span>
      <p class="details__origin">MADE IN AUSTRALIA</p>
      <p class="details__volume">250 ML.</p>
    </footer>
  </article>

  <article class="label label--caribbean">
    <div class="label__pattern" role="img" aria-label="Faint white tropical palm and monstera leaf pattern"></div>
    <div class="brand">Dawn Meadow</div>
    <section class="band">
      <p class="band__variant band__variant--spaced">CARIBBEAN</p>
      <h2 class="band__title">BODY<br>WASH</h2>
      <div class="band__art" role="img" aria-label="White line drawing of a bird of paradise flower"></div>
    </section>
    <footer class="details">
      <p class="details__claim">NATURAL RAW HONEY &amp; GOATS MILK</p>
      <span class="details__map" role="img" aria-label="Small map of Australia"></span>
      <p class="details__origin">MADE IN AUSTRALIA</p>
      <p class="details__volume">250 ML.</p>
    </footer>
  </article>

  <article class="label label--natural">
    <div class="label__pattern" role="img" aria-label="Faint white wildflower and grass stem pattern"></div>
    <div class="brand">Dawn Meadow</div>
    <section class="band">
      <p class="band__variant band__variant--spaced">NATURAL</p>
      <h2 class="band__title">BODY<br>WASH</h2>
      <div class="band__art" role="img" aria-label="White line drawing of a berry sprig"></div>
    </section>
    <footer class="details">
      <p class="details__claim">NATURAL RAW HONEY &amp; GOATS MILK</p>
      <span class="details__map" role="img" aria-label="Small map of Australia"></span>
      <p class="details__origin">MADE IN AUSTRALIA</p>
      <p class="details__volume">250 ML.</p>
    </footer>
  </article>

</main>
</body>
</html>
```